Business Cards for a Junk Removal Company

Hello,
We are looking to have business cards designed that are simple, bold, easy to read, and right to the point. Please see the attachments for our logo files. We want the card to be yellow on both sides ( Color code Yellow: #FFE01B). The logo text font is (Rockstar Extra Bold) and this is also in the files attached. Please make the text black for the logo. On the back side of the card, you can use white and black for text. Thank you in advance for your hard work!

Front of card-
Harbor Haul Away (logo)
Back of card-
Harbor Haul Away
Donate - Recycle - Dispose
555-271-8093
www.harborhaulaway.example
info@harborhaulaway.example

Industry/Entity Type

Junk removal

Contact Information for Business Card

FRONT OF CARD- Harbor Haul Away (logo) BACK OF CARD- Harbor Haul Away Donate - Recycle - Dispose 555-271-8093 www.harborhaulaway.example info@harborhaulaway.example

Font styles to use
Other font styles liked:
• Rockstar Extra Bold

Colors
FFF300
FFF600
FEFA6F
FFFEC7
FFFEE8

Requirements
Must have
• Must have color code Yellow: #FFE01B for the background of front and back of the card

```html
<!DOCTYPE html>
<html lang="en">
<head>
<meta charset="utf-8">
<title>Harbor Haul Away – Business Cards</title>
<link rel="stylesheet" href="https://fonts.googleapis.com/css2?family=Anton&family=Arimo:wght@400;700&display=swap">
<style>
  :root {
    --card-yellow: #FFE01B;
    --ink: #000000;
    --backdrop: #8c8c8c;
    --card-shadow: rgba(0, 0, 0, 0.35);
  }
  * { margin: 0; padding: 0; box-sizing: border-box; }
  html, body { width: 1200px; height: 800px; overflow: hidden; }
  body {
    background: var(--backdrop);
    display: flex;
    align-items: center;
    justify-content: center;
    gap: 40px;
    font-family: "Arimo", Arial, sans-serif;
    color: var(--ink);
  }
  .card {
    position: relative;
    width: 540px;
    height: 309px;
    background: var(--card-yellow);
    box-shadow: 0 6px 16px var(--card-shadow);
  }
  .brand-name {
    font-family: "Anton", Impact, sans-serif;
    font-weight: 400;
    text-transform: uppercase;
    line-height: 1;
    white-space: nowrap;
    color: var(--ink);
  }

  /* Contact side */
  .card--contact .brand-name {
    position: absolute;
    top: 44px;
    right: 40px;
    font-size: 30px;
  }
  .person {
    position: absolute;
    left: 40px;
    top: 104px;
  }
  .person-name {
    font-family: "Anton", Impact, sans-serif;
    font-size: 26px;
    text-transform: uppercase;
    line-height: 1;
  }
  .person-title { font-size: 14px; margin-top: 4px; }

  .divider {
    position: absolute;
    left: 40px;
    right: 30px;
    top: 160px;
    height: 1px;
    background: var(--ink);
  }

  .tagline {
    position: absolute;
    right: 30px;
    top: 176px;
    font-family: "Anton", Impact, sans-serif;
    font-size: 15px;
    letter-spacing: 0.8px;
    text-transform: uppercase;
  }

  .contact-list {
    position: absolute;
    left: 40px;
    top: 176px;
    list-style: none;
    font-size: 14px;
    line-height: 1;
  }
  .contact-list li {
    display: flex;
    align-items: center;
    gap: 8px;
    margin-bottom: 10px;
  }
  .contact-list .phone { font-size: 18px; }
  .contact-icon { width: 12px; height: 12px; flex: none; }

  /* Logo side */
  .card--logo {
    display: flex;
    align-items: center;
    justify-content: center;
  }
  .card--logo .brand-name { font-size: 54px; }
</style>
</head>
<body>

  <section class="card card--contact" aria-label="Business card, contact side">
    <p class="brand-name">Harbor Haul Away</p>

    <div class="person">
      <p class="person-name">Dana Reyes</p>
      <p class="person-title">CEO&amp;Founder</p>
    </div>

    <div class="divider"></div>

    <ul class="contact-list">
      <li class="phone">
        <svg class="contact-icon" viewBox="0 0 24 24" aria-hidden="true"><path fill="currentColor" d="M6.6 10.8a15.1 15.1 0 0 0 6.6 6.6l2.2-2.2c.3-.3.7-.4 1-.2 1.1.4 2.300.6 3.6.6.6 0 1 .4 1 1V20c0 .6-.4 1-1 1A17 17 0 0 1 3 4c0-.6.4-1 1-1h3.5c.6 0 1 .4 1 1 0 1.3.2 2.5.6 3.6.1.3 0 .7-.2 1z"/></svg>
        555-271-8093
      </li>
      <li>
        <svg class="contact-icon" viewBox="0 0 24 24" aria-hidden="true"><path fill="currentColor" d="M2 5h20v14H2z"/><path fill="none" stroke="#FFE01B" stroke-width="2" d="M2 5l10 8 10-8"/></svg>
        info@harborhaulaway.example
      </li>
      <li>
        <svg class="contact-icon" viewBox="0 0 24 24" aria-hidden="true"><circle cx="12" cy="12" r="10" fill="none" stroke="currentColor" stroke-width="2.5"/><path fill="none" stroke="currentColor" stroke-width="2" d="M2 12h20M12 2c3 3 3 17 0 20M12 2c-3 3-3 17 0 20"/></svg>
        www.harborhaulaway.example
      </li>
    </ul>

    <p class="tagline">Donate - Recycle - Dispose</p>
  </section>

  <section class="card card--logo" aria-label="Business card, logo side">
    <p class="brand-name">Harbor Haul Away</p>
  </section>

</body>
</html>
```